PowerPoint Design Project

Lanterfield Estate Partners is a Melbourne based property development management company. We provide a comprehensive range of development management services to a select group of listed developers, private landowners, overseas investors and development partners and institutional clients. Our website provides additional information about the company:
http://www.lanterfieldep.example.au
We are looking for a versatile powerpoint design that can be used across a wide variety of presentations including; pitch documents, client reports, Information memorandums, and downloadable credential packs etc. We have attached a good example document.
Updates

Industry/Entity Type

It Company

Requirements
Must have
• The design should have the following slides as a minimum: Intro Page, transition slides, profile slides, slides for graphics,

```html
<!DOCTYPE html>
<html lang="en">
<head>
<meta charset="utf-8">
<title>Lanterfield Estate Partners – Presentation Template</title>
<link href="https://fonts.googleapis.com/css2?family=Arimo:wght@400;700&display=swap" rel="stylesheet">
<style>
:root{
  --ink:#1a1a1a;
  --title-grey:#8c8c8c;
  --band:#e4e4e4;
  --band-light:#f1f1f1;
  --footer:#d2d2d2;
  --frame:#3a3a3a;
  --gold:#f5aa00;
  --gold-mid:#fcc350;
  --gold-pale:#fde4a8;
  --gold-soft:#feeecb;
}
*{margin:0;padding:0;box-sizing:border-box}
html,body{width:1200px;height:849px;overflow:hidden;background:#fff}
body{position:relative;font-family:"Arimo",Arial,sans-serif;color:var(--ink)}
.slide{position:absolute;width:317px;height:237px;border:1px solid var(--frame);background:#fff;overflow:hidden}
.art{position:absolute;inset:0;width:100%;height:100%}
.brand{position:absolute;font-weight:700;font-size:7px;letter-spacing:.2px;color:var(--ink);white-space:nowrap}
.brand.top{top:20px;right:14px}
.brand.bottom{top:210px;left:18px}
.section-title{position:absolute;left:142px;top:167px;font-size:11px;font-weight:700;color:var(--title-grey);letter-spacing:.3px}
.rule{position:absolute;left:140px;right:0;top:184px;height:1px;background:#cfcfcf}
.head-title{position:absolute;left:12px;top:16px;font-size:12px;font-weight:700;color:var(--title-grey);letter-spacing:.3px}
.footer-text{position:absolute;top:219px;left:190px;font-size:4.5px;color:#333}
.page-no{position:absolute;top:219px;right:14px;font-size:4.5px;color:#333}
.lead{position:absolute;font-size:8.5px;line-height:1.2}
.body{position:absolute;font-size:5px;line-height:1.3}
.body p{margin-bottom:5px}
.services{list-style:none}
.services li::before{content:"•";margin-right:4px}
.tile{position:absolute;top:102px;width:52px;height:87px}
.tile .caption{position:absolute;bottom:0;left:0;right:0;height:15px;background:#3b3b3b;color:#fff;font-size:4px;text-align:center;line-height:1.1;display:flex;align-items:center;justify-content:center}
.donut-label{position:absolute;font-size:5px;font-weight:700;text-align:center;line-height:1.2}
</style>
</head>
<body>
<svg width="0" height="0" style="position:absolute">
  <defs>
    <linearGradient id="streetscape" x1="0" y1="0" x2="0" y2="1">
      <stop offset="0" stop-color="#c9dbe8"/><stop offset=".45" stop-color="#d9d2c4"/><stop offset=".75" stop-color="#7e8f5a"/><stop offset="1" stop-color="#5e7240"/>
    </linearGradient>
    <linearGradient id="parkland" x1="0" y1="0" x2="0" y2="1">
      <stop offset="0" stop-color="#b9c7b0"/><stop offset=".5" stop-color="#6f7a4c"/><stop offset="1" stop-color="#8c8b55"/>
    </linearGradient>
    <linearGradient id="grassland" x1="0" y1="0" x2="0" y2="1">
      <stop offset="0" stop-color="#a9a487"/><stop offset=".5" stop-color="#786c4a"/><stop offset="1" stop-color="#8a8a5a"/>
    </linearGradient>
    <linearGradient id="homes" x1="0" y1="0" x2="1" y2="0">
      <stop offset="0" stop-color="#d8c7a6"/><stop offset=".6" stop-color="#c9a57a"/><stop offset="1" stop-color="#e6dfd2"/>
    </linearGradient>
  </defs>
</svg>

<!-- Intro -->
<section class="slide" style="left:97px;top:47px">
  <svg class="art" viewBox="0 0 317 237">
    <polygon points="130,78 317,78 317,135 90,135" fill="var(--band-light)"/>
    <polygon points="150,78 180,78 135,120 105,120" fill="#e2e2e2"/>
    <polygon points="0,78 150,78 110,135 0,135" fill="url(#homes)" role="img" aria-label="Photograph of new townhouses"/>
    <line x1="68" y1="168" x2="317" y2="168" stroke="#cfcfcf" stroke-width="1"/>
  </svg>
  <div class="brand top">LANTERFIELD ESTATE PARTNERS</div>
  <div style="position:absolute;left:68px;top:148px;font-size:13px;color:var(--title-grey)">Presentation title here</div>
  <div style="position:absolute;left:68px;top:175px;font-size:9px;font-weight:700">date</div>
</section>

<!-- Transition: About us -->
<section class="slide" style="left:453px;top:47px">
  <svg class="art" viewBox="0 0 317 237">
    <polygon points="0,0 317,0 317,143 145,143 100,187 0,187" fill="url(#streetscape)" role="img" aria-label="Photograph of a residential street with homes and park"/>
    <polygon points="145,143 185,143 140,187 100,187" fill="#e8e8e8" opacity=".8"/>
  </svg>
  <div class="section-title">ABOUT US</div><div class="rule"></div>
  <div class="brand bottom">LANTERFIELD ESTATE PARTNERS</div>
</section>

<!-- About us profile -->
<section class="slide" style="left:799px;top:47px">
  <svg class="art" viewBox="0 0 317 237">
    <polygon points="0,0 230,0 190,42 0,42" fill="var(--band)"/>
    <polygon points="230,0 262,0 222,42 190,42" fill="var(--band-light)"/>
    <polygon points="0,95 150,95 105,237 0,237" fill="url(#streetscape)" role="img" aria-label="Photograph of two-storey townhouses"/>
    <polygon points="60,237 95,208 130,208 100,237" fill="var(--band-light)"/>
    <polygon points="100,237 130,208 317,208 317,237" fill="var(--footer)"/>
  </svg>
  <div class="head-title">ABOUT US</div>
  <div class="brand top" style="top:28px">LANTERFIELD ESTATE PARTNERS</div>
  <div class="lead" style="left:20px;top:50px;width:140px">LANTERFIELD is a boutique property development company based in Melbourne.</div>
  <div class="body" style="left:158px;top:90px;width:148px">
    <p>LANTERFIELD undertakes its own developments and also provides a comprehensive range of development management services to a select group of listed developers, private landowners, overseas investors and development partners.</p>
    <p>LANTERFIELD has a track record in identifying and acquiring development sites, matching project opportunities with capital partners, managing complex planning approvals and delivering commercially successful development projects.</p>
    <p>LANTERFIELD has specialist capabilities to provide development management services at any stage in a property development's life-cycle.</p>
  </div>
  <div class="footer-text">PRESENTATION FOOTER</div><div class="page-no">3</div>
</section>

<!-- Transition: What we do -->
<section class="slide" style="left:97px;top:317px">
  <svg class="art" viewBox="0 0 317 237">
    <polygon points="0,0 317,0 317,143 145,143 100,187 0,187" fill="url(#streetscape)" role="img" aria-label="Photograph of large family homes with gardens"/>
    <polygon points="145,143 185,143 140,187 100,187" fill="#e8e8e8" opacity=".8"/>
  </svg>
  <div class="section-title">WHAT WE DO</div><div class="rule"></div>
  <div class="brand bottom">LANTERFIELD ESTATE PARTNERS</div>
</section>

<!-- What we do profile -->
<section class="slide" style="left:453px;top:317px">
  <svg class="art" viewBox="0 0 317 237">
    <polygon points="0,0 230,0 190,42 0,42" fill="var(--band)"/>
    <polygon points="230,0 262,0 222,42 190,42" fill="var(--band-light)"/>
    <polygon points="0,110 155,110 155,200 115,237 0,237" fill="url(#parkland)" role="img" aria-label="Photograph of a tree-lined estate road"/>
    <polygon points="100,237 130,208 317,208 317,237" fill="var(--footer)"/>
    <polygon points="115,237 145,208 175,208 145,237" fill="var(--band-light)" opacity=".7"/>
  </svg>
  <div class="head-title">WHAT WE DO</div>
  <div class="brand top" style="top:28px">LANTERFIELD ESTATE PARTNERS</div>
  <div class="lead" style="left:12px;top:54px;width:150px;font-size:6.8px">LANTERFIELD has significant experience in real estate development and our expertise spans Real Estate Advisory, Acquisitions &amp; Divestments, Development Management and Marketing &amp; Sales Management.</div>
  <div class="body" style="left:170px;top:88px;width:140px">
    <p>Our end-to-end development management services include:</p>
    <ul class="services">
      <li>Acquisition &amp; Due Diligence</li><li>Project Vision &amp; Concept Design</li><li>Project Approvals</li><li>Financial &amp; Value Management</li><li>Marketing &amp; Sales</li><li>Project Funding</li><li>Construction &amp; Delivery</li><li>Transaction Management</li><li>Project Completion &amp; Divestment</li>
    </ul>
  </div>
  <div class="footer-text">PRESENTATION FOOTER</div><div class="page-no">5</div>
</section>

<!-- Transition: Our expertise -->
<section class="slide" style="left:799px;top:317px">
  <svg class="art" viewBox="0 0 317 237">
    <polygon points="0,0 317,0 317,143 145,143 100,187 0,187" fill="url(#parkland)" role="img" aria-label="Photograph of palm trees in front of estate homes"/>
    <polygon points="145,143 185,143 140,187 100,187" fill="#e8e8e8" opacity=".8"/>
  </svg>
  <div class="section-title">OUR EXPERTISE</div><div class="rule"></div>
  <div class="brand bottom">LANTERFIELD ESTATE PARTNERS</div>
</section>

<!-- Our expertise chart -->
<section class="slide" style="left:97px;top:586px">
  <svg class="art" viewBox="0 0 317 237">
    <polygon points="0,0 230,0 190,42 0,42" fill="var(--band)"/>
    <polygon points="230,0 262,0 222,42 190,42" fill="var(--band-light)"/>
    <path d="M92,124 A65,65 0 0 1 157,59 L157,104 A20,20 0 0 0 137,124 Z" fill="var(--gold)"/>
    <path d="M159,59 A65,65 0 0 1 224,124 L179,124 A20,20 0 0 0 159,104 Z" fill="var(--gold-pale)"/>
    <path d="M92,126 A65,65 0 0 0 157,191 L157,146 A20,20 0 0 1 137,126 Z" fill="var(--gold-soft)"/>
    <path d="M224,126 A65,65 0 0 1 159,191 L159,146 A20,20 0 0 0 179,126 Z" fill="var(--gold-mid)"/>
    <polygon points="100,237 130,208 317,208 317,237" fill="var(--footer)"/>
    <polygon points="70,237 100,208 130,208 100,237" fill="var(--band-light)"/>
  </svg>
  <div class="head-title">OUR EXPERTISE</div>
  <div class="brand top" style="top:28px">LANTERFIELD ESTATE PARTNERS</div>
  <div class="donut-label" style="left:108px;top:88px">Real Estate<br>Advisory</div>
  <div class="donut-label" style="left:163px;top:88px">Acquisitions &amp;<br>Divestments</div>
  <div class="donut-label" style="left:106px;top:151px">Development<br>Management</div>
  <div class="donut-label" style="left:165px;top:151px">Marketing &amp; Sales<br>Management</div>
  <div class="footer-text">PRESENTATION FOOTER</div><div class="page-no">7</div>
</section>

<!-- Transition: Project experience -->
<section class="slide" style="left:453px;top:586px">
  <svg class="art" viewBox="0 0 317 237">
    <polygon points="0,0 317,0 317,143 145,143 100,187 0,187" fill="url(#grassland)" role="img" aria-label="Photograph of native grasses along an estate road"/>
    <polygon points="145,143 185,143 140,187 100,187" fill="#e8e8e8" opacity=".8"/>
  </svg>
  <div class="section-title">PROJECT EXPERIENCE</div><div class="rule"></div>
  <div class="brand bottom">LANTERFIELD ESTATE PARTNERS</div>
</section>

<!-- Project experience -->
<section class="slide" style="left:799px;top:586px">
  <svg class="art" viewBox="0 0 317 237">
    <polygon points="0,0 230,0 190,42 0,42" fill="var(--band)"/>
    <polygon points="230,0 262,0 222,42 190,42" fill="var(--band-light)"/>
    <polygon points="100,237 130,208 317,208 317,237" fill="var(--footer)"/>
    <polygon points="70,237 100,208 130,208 100,237" fill="var(--band-light)"/>
  </svg>
  <div class="head-title">PROJECT EXPERIENCE</div>
  <div class="brand top" style="top:28px">LANTERFIELD ESTATE PARTNERS</div>
  <div class="lead" style="left:12px;top:62px;width:190px;font-size:6.8px">LANTERFIELD is experienced in creating and delivering market leading and commercially successful residential and mixed use developments.</div>
  <div class="tile" style="left:12px"><div role="img" aria-label="Photograph of a master planned community" style="height:72px;background:linear-gradient(#c9d6e2,#9aa08a)"></div><div class="caption">Master Planned<br>Communities</div></div>
  <div class="tile" style="left:72px"><div role="img" aria-label="Aerial photograph of a land subdivision" style="height:72px;background:linear-gradient(#8b8467,#6a6a4e)"></div><div class="caption">Land Subdivisions</div></div>
  <div class="tile" style="left:131px"><div role="img" aria-label="Photograph of integrated housing with palms" style="height:72px;background:linear-gradient(#b7c2c6,#6e7a48)"></div><div class="caption">Integrated Housing</div></div>
  <div class="tile" style="left:189px"><div role="img" aria-label="Photograph of a residential golf community" style="height:72px;background:linear-gradient(#c5d3dc,#7c9a4a)"></div><div class="caption">Residential Golf<br>Communities</div></div>
  <div class="tile" style="left:247px"><div role="img" aria-label="Photograph of medium density built form" style="height:72px;background:linear-gradient(#c8d6e4,#6f8a46)"></div><div class="caption">Medium Density &amp;<br>Built Form</div></div>
  <div class="footer-text">PRESENTATION FOOTER</div><div class="page-no">9</div>
</section>
</body>
</html>
```